A4 Single Sided Brochure Folder Design Technical Company

We are a technical company based in the UK, working worldwide for Power Distribution companies.

We have technical literature and need a folder to present these in. The design should be very simple and clean using our logo and "Innovative Utility Solutions"

Our website brenvox.com gives and idea of the business but don't follow the look of the website as we will be redoing shortly.

Requirements
Must have
• Logo and Strap Line
Nice to have
• Clean, easy to print and timeless
Should not have
• Shouldn't be fashionable, we certainly aren't

```html
<!DOCTYPE html>
<html lang="en">
<head>
<meta charset="UTF-8">
<title>Brenvox – Innovative Utility Solutions Folder</title>
<link href="https://fonts.googleapis.com/css2?family=Roboto:wght@700;900&family=Open+Sans:wght@300;400&display=swap" rel="stylesheet">
<style>
  :root {
    --magenta: #b0206f;
    --magenta-deep: #9c1a60;
    --paper: #ececec;
    --ink: #1a1a1a;
    --blue: #1a8ede;
    --green: #2e9e3e;
    --backdrop: #9a9a9a;
  }
  * { margin: 0; padding: 0; box-sizing: border-box; }
  html, body { width: 1200px; height: 1200px; overflow: hidden; }
  body {
    background: var(--backdrop);
    display: flex; align-items: center; justify-content: center;
    font-family: "Open Sans", sans-serif;
  }
  .folder-cover {
    position: relative;
    width: 780px; height: 1104px;
    background: var(--paper);
    overflow: hidden;
  }
  .top-band {
    position: absolute; left: 0; top: 0; width: 100%; height: 110px;
    background: linear-gradient(90deg, var(--magenta-deep), var(--magenta));
  }
  .brand-name {
    position: absolute; left: 0; right: 0; top: 118px;
    text-align: center; padding-left: 240px;
    font-family: "Open Sans", sans-serif; font-weight: 300;
    font-size: 38px; color: var(--magenta); letter-spacing: 1px;
  }
  .headline {
    position: absolute; right: 60px; top: 178px; text-align: right;
    font-family: "Roboto", sans-serif; line-height: 1;
  }
  .headline .lead { font-weight: 900; font-size: 40px; color: var(--ink); letter-spacing: 0.5px; }
  .headline .key { font-weight: 900; font-size: 78px; color: var(--blue); letter-spacing: 1px; margin-top: 2px; }
  .rule { position: absolute; left: 0; width: 100%; height: 12px; background: var(--magenta); }
  .rule.above-photo { top: 300px; }
  .rule.below-photo { top: 766px; }
  .photo-area {
    position: absolute; left: 0; top: 312px; width: 100%; height: 454px;
    background: linear-gradient(135deg, #d9d9dc 0%, #eeeeef 45%, #bfc0c3 100%);
  }
  .statement {
    position: absolute; left: 70px; right: 70px; top: 820px;
    font-size: 19px; line-height: 1.35; color: var(--ink); text-align: center;
  }
  .quote-mark { position: absolute; width: 44px; height: 34px; }
  .quote-mark.open { left: 40px; top: 800px; }
  .quote-mark.close { right: 40px; top: 930px; }
  .web-bar {
    position: absolute; left: 230px; top: 930px; width: 300px; height: 30px;
    background: var(--green); color: var(--magenta);
    font-size: 17px; line-height: 30px; text-align: center;
  }
  .bottom-band {
    position: absolute; left: 0; bottom: 0; width: 100%; height: 100px;
    background: linear-gradient(90deg, var(--magenta), var(--magenta-deep));
  }
  .bottom-band::before {
    content: ""; position: absolute; left: 0; top: -24px; width: 100%; height: 24px; background: var(--paper);
  }
</style>
</head>
<body>
  <main class="folder-cover">
    <div class="top-band"></div>
    <div class="brand-name">Brenvox</div>
    <h1 class="headline">
      <div class="lead">INNOVATIVE UTILITY</div>
      <div class="key">SOLUTIONS</div>
    </h1>
    <div class="rule above-photo"></div>
    <div class="photo-area" role="img" aria-label="Photograph of a laboratory gas sampling panel with flow meters, pressure gauges, valves and red tubing"></div>
    <div class="rule below-photo"></div>

    <svg class="quote-mark open" viewBox="0 0 44 34" aria-hidden="true">
      <path d="M4 34 V18 Q4 4 18 0 L19 6 Q11 9 11 16 H19 V34 Z M25 34 V18 Q25 4 39 0 L40 6 Q32 9 32 16 H40 V34 Z" fill="var(--magenta)"/>
    </svg>
    <p class="statement">Brenvox Limited is an independent company providing specialist services to the utility, oil and gas and infrastructure sectors, worldwide.</p>
    <svg class="quote-mark close" viewBox="0 0 44 34" aria-hidden="true">
      <path d="M40 0 V16 Q40 30 26 34 L25 28 Q33 25 33 18 H25 V0 Z M19 0 V16 Q19 30 5 34 L4 28 Q12 25 12 18 H4 V0 Z" fill="var(--magenta)"/>
    </svg>
    <div class="web-bar">www.brenvox.com</div>

    <div class="bottom-band"></div>
  </main>
</body>
</html>
```